Exhibition Stand Design for innovative Social Business

We are an innovative social business empowering people to value nature through ZUN, a complementary digital currency. We have attached the TEK_ZUN branding document, and are needing a design for our exhibition stand (https://fairbuildlab.com/produit/stand-parapluie-classic-pvc-3x4c/. The attached doc mocks up a stand on page 32, though we would like some messaging included, in line with our website www.tekzun.ch. You will see there how the branding concept has been implemented with the TEK:GROW, SHARE, THRIVE wording, as well as everyone gains. Our green colours are included in the branding document. Many thanks!

Industry/Entity Type

Environment

Font styles to use
Other font styles liked:
• As per our attached fonts

Requirements
Must have
• Our attached branding guidelines gives our look and feel - Innovative / Dynamic / Vibrant / Reliable / Accessible / Connected.

```html
<!DOCTYPE html>
<html lang="en">
<head>
<meta charset="utf-8">
<title>TEK ZUN – Exhibition Stand</title>
<link href="https://fonts.googleapis.com/css2?family=Montserrat:wght@800&family=Lexend:wght@500;600&display=swap" rel="stylesheet">
<style>
  :root {
    --bg-left: #5ce9c9;
    --bg-right: #22f034;
    --bubble: rgba(255, 255, 255, 0.32);
    --bubble-strong: rgba(255, 255, 255, 0.78);
    --ink: #0b0b0b;
    --label-green: #1fe832;
    --tag-green: #2fe06a;
    --copy-green: #1b5a28;
  }
  * { margin: 0; padding: 0; box-sizing: border-box; }
  html, body { width: 1200px; height: 849px; overflow: hidden; }
  body { background: #ffffff; }
  .stand-panel {
    position: relative;
    width: 1200px;
    height: 849px;
    overflow: hidden;
    background: linear-gradient(90deg, var(--bg-left) 0%, #3ceb8c 45%, var(--bg-right) 100%);
    font-family: "Lexend", sans-serif;
  }
  .stand-panel__art { position: absolute; inset: 0; }
  .brand-name {
    position: absolute;
    top: 38px;
    left: 0;
    width: 1200px;
    text-align: center;
    font-family: "Montserrat", sans-serif;
    font-weight: 800;
    font-size: 98px;
    letter-spacing: -2px;
    line-height: 1;
    color: var(--ink);
  }
  .tagline {
    position: absolute;
    top: 146px;
    left: 0;
    width: 1200px;
    text-align: center;
    font-weight: 600;
    font-size: 36px;
    line-height: 1;
    color: var(--ink);
  }
  .concept-prefix {
    position: absolute;
    top: 222px;
    left: 58px;
    width: 192px;
    text-align: center;
    font-family: "Montserrat", sans-serif;
    font-weight: 800;
    font-size: 58px;
    line-height: 1;
    color: var(--tag-green);
  }
  .pillar-label {
    position: absolute;
    top: 466px;
    width: 320px;
    text-align: center;
    font-family: "Montserrat", sans-serif;
    font-weight: 800;
    font-size: 54px;
    letter-spacing: -1px;
    line-height: 1;
    color: var(--label-green);
  }
  .pillar-label--grow { left: 144px; }
  .pillar-label--share { left: 442px; }
  .pillar-label--thrive { left: 754px; }
  .message {
    position: absolute;
    top: 603px;
    left: 0;
    width: 1200px;
    text-align: center;
    font-weight: 600;
    font-size: 26px;
    line-height: 28px;
    color: var(--copy-green);
  }
  .message__closing { margin-top: 26px; }
</style>
</head>
<body>
<main class="stand-panel">
  <svg class="stand-panel__art" width="1200" height="849" viewBox="0 0 1200 849">
    <defs>
      <linearGradient id="photo-grow" x1="0" y1="0" x2="1" y2="1">
        <stop offset="0" stop-color="#ece6e0"/>
        <stop offset="0.55" stop-color="#c0704a"/>
        <stop offset="1" stop-color="#f1ece8"/>
      </linearGradient>
      <linearGradient id="photo-share" x1="0" y1="0" x2="1" y2="1">
        <stop offset="0" stop-color="#b8cfa8"/>
        <stop offset="0.45" stop-color="#7fd79a"/>
        <stop offset="1" stop-color="#a9884f"/>
      </linearGradient>
      <linearGradient id="photo-thrive" x1="0" y1="0" x2="0" y2="1">
        <stop offset="0" stop-color="#bff1e2"/>
        <stop offset="0.35" stop-color="#4fb070"/>
        <stop offset="1" stop-color="#1f7a36"/>
      </linearGradient>
    </defs>
    <circle class="bubble" cx="868" cy="76" r="112" fill="var(--bubble)"/>
    <circle class="bubble" cx="216" cy="616" r="156" fill="var(--bubble)"/>
    <circle class="bubble" cx="908" cy="664" r="252" fill="var(--bubble)"/>
    <circle class="photo" cx="300" cy="404" r="158" fill="url(#photo-grow)" role="img" aria-label="Photo: young woman with long auburn hair looking to the side"/>
    <circle class="photo" cx="914" cy="400" r="156" fill="url(#photo-thrive)" role="img" aria-label="Photo: rolling green hills under a pale sky"/>
    <circle class="photo" cx="602" cy="400" r="178" fill="url(#photo-share)" role="img" aria-label="Photo: hand holding a smartphone with the payment app next to a countertop payment terminal"/>
    <circle class="bubble bubble--prefix" cx="154" cy="252" r="96" fill="var(--bubble-strong)"/>
  </svg>

  <h1 class="brand-name">TEK ZUN</h1>
  <p class="tagline">everyone gains</p>

  <p class="concept-prefix">OUR</p>
  <p class="pillar-label pillar-label--grow">GROW</p>
  <p class="pillar-label pillar-label--share">SHARE</p>
  <p class="pillar-label pillar-label--thrive">THRIVE</p>

  <div class="message">
    <p>Join our growing ecosystem of communities<br>and businesses in a movement to value nature.</p>
    <p class="message__closing">Better for you<br>Better for the planet!</p>
  </div>
</main>
</body>
</html>
```